Dale Hornsby's Swingcraft Big Band — Hot & Sticky ------ CD Cover Art (and Disc Art)

Need a front cover jacket and a disc design for a fantastic all-pro big band (jazz/funk/reggae) CD. We really want to use a group photo somehow since so many of the band members are world famous, LA's finest studio musicians with mostly original music arranged by the biggest names in jazz. Playful, fun, lighthearted, tasteful arrangements with world class soloists.

Target Market(s)

Music/Jazz/Big band enthusiasts; other musicians

Other font styles liked:
• See uploaded file #4

Colors

Designer to choose colors to be used in the design.

Requirements
Must have
• Legibility . . . must be easy to read and not crowded or cluttered. Font idea below (A Quiet Night Beneath The Tangled Pines) is for feel and flavor. It is absolutely not necessary to match if you have something you like better.
Nice to have
• Colorful but not tacky. Maybe a play on the CD title, Hot and Sticky?

```html
<!DOCTYPE html>
<html lang="en">
<head>
<meta charset="utf-8">
<title>Dale Hornsby's Swingcraft Big Band — Hot &amp; Sticky</title>
<link rel="stylesheet" href="https://fonts.googleapis.com/css2?family=Bowlby+One&family=Open+Sans:wght@400;700&display=swap">
<style>
  :root {
    --ink: #0c0c0c;
    --ink-soft: #1c1c1c;
    --ink-sheen: #2a2a2a;
    --gold: #e4bd3f;
    --gold-deep: #b08a22;
    --gold-light: #f0d267;
    --red: #d43a4c;
    --white: #ffffff;
    --photo-warm: #8a5a3a;
    --photo-dark: #2b2320;
    --photo-rose: #a8465a;
  }
  * { margin: 0; padding: 0; box-sizing: border-box; }
  html, body {
    width: 1200px;
    height: 1200px;
    overflow: hidden;
    background: var(--ink);
  }
  .cover {
    position: relative;
    width: 1200px;
    height: 1200px;
    overflow: hidden;
    background:
      repeating-linear-gradient(100deg, transparent 0 14px, rgba(255,255,255,0.025) 14px 16px, transparent 16px 38px),
      linear-gradient(180deg, var(--ink) 0%, var(--ink-soft) 35%, var(--ink) 60%);
  }
  .cover__masthead {
    position: absolute;
    left: 70px;
    top: 60px;
    font-family: "Bowlby One", "Arial Black", sans-serif;
    line-height: 1;
    text-shadow: 2px 3px 0 rgba(0,0,0,0.6);
  }
  .masthead__leader {
    display: block;
    color: var(--gold);
    font-size: 84px;
    letter-spacing: 1px;
  }
  .masthead__band {
    display: block;
    color: var(--white);
    font-size: 50px;
    margin: 8px 0 0 90px;
  }
  .masthead__album {
    display: block;
    color: var(--red);
    font-size: 74px;
    margin: 6px 0 0 90px;
  }
  .rule {
    position: absolute;
    left: 0;
    width: 100%;
    background: var(--red);
  }
  .rule--upper { top: 318px; height: 10px; }
  .rule--lower { top: 1012px; height: 10px; }
  .band-photo {
    position: absolute;
    left: 0;
    top: 348px;
    width: 100%;
    height: 550px;
    background:
      radial-gradient(ellipse at 70% 15%, var(--photo-rose) 0%, transparent 45%),
      radial-gradient(ellipse at 30% 85%, var(--photo-warm) 0%, transparent 55%),
      linear-gradient(180deg, #5e4b45 0%, var(--photo-dark) 55%, #6b4a30 100%);
  }
  .strip {
    position: absolute;
    left: 0;
    top: 898px;
    width: 100%;
    height: 114px;
    background: var(--ink);
  }
  .gold-band {
    position: absolute;
    left: 0;
    top: 1022px;
    width: 100%;
    height: 178px;
    background:
      repeating-linear-gradient(95deg, transparent 0 22px, rgba(255,255,255,0.06) 22px 25px, transparent 25px 60px),
      linear-gradient(180deg, var(--gold-light) 0%, var(--gold) 45%, var(--gold-deep) 100%);
  }
  .track-title {
    position: absolute;
    left: 0;
    top: 928px;
    width: 100%;
    text-align: center;
    font-family: "Open Sans", Arial, sans-serif;
    font-size: 44px;
    line-height: 1.2;
  }
  .track-title__lead {
    color: var(--white);
    font-weight: 400;
    margin-right: 14px;
  }
  .track-title__main {
    color: var(--gold);
    font-weight: 700;
  }
</style>
</head>
<body>
  <main class="cover">
    <h1 class="cover__masthead">
      <span class="masthead__leader">Dale Hornsby's</span>
      <span class="masthead__band">Swingcraft Big Band</span>
      <span class="masthead__album">Hot &amp; Sticky</span>
    </h1>

    <div class="rule rule--upper"></div>
    <div class="band-photo" role="img" aria-label="Group photo of the big band posing with their instruments and music stands in a recording studio"></div>
    <div class="strip"></div>

    <p class="track-title">
      <span class="track-title__lead">A Quiet Night Beneath</span><span class="track-title__main">The Tangled Pines</span>
    </p>

    <div class="rule rule--lower"></div>
    <div class="gold-band"></div>
  </main>
</body>
</html>
```